business cards for heating company

I need business cards for my heating air conditioning and chimney company located in upstate NY I would like for them to be colorful and catchy on heavy stock with preferably a glossy finish on front of card but the ability to write something on one half of the back with maybe some bullets on the other half of the back I also need to be able to change the name and title of employees on the card and also incorporate some of our current look and feel from our trucks and website I also want to be able to use this design or similar to have door hangers made lawn signs coffee mugs key chains etc. our website is Brindlecove.com

Target Market(s)

homeowners

Industry/Entity Type

Air Conditioning

Contact Information for Business Card

should have website brindlecove.com , phone number 585-437-9168 please look at website for ideas

Font styles to use
Sans Serif

Colors
ec1f27
3176b5
fbee3f

Requirements
Must have
• a complete look
Nice to have
• a discount offer like 10% military and first responders
• senior discount %5

```html
<!DOCTYPE html>
<html lang="en">
<head>
<meta charset="utf-8">
<title>Brindle Cove – Business Cards</title>
<link href="https://fonts.googleapis.com/css2?family=Jost:wght@400;500;700&display=swap" rel="stylesheet">
<style>
  :root {
    --page-bg: #e9e6e1;
    --card-bg: #ffffff;
    --card-shade: #f1f1f1;
    --brand-red: #d8334a;
    --accent-red: #ec1f27;
    --brand-blue: #1f4f8f;
    --ink: #2b2b2b;
    --soft-white: #dfe6f2;
  }
  html, body {
    margin: 0;
    width: 1200px;
    height: 904px;
    overflow: hidden;
    background: var(--page-bg);
    font-family: "Jost", sans-serif;
  }
  .canvas {
    position: relative;
    width: 1200px;
    height: 904px;
  }
  .card {
    position: absolute;
    width: 560px;
    height: 320px;
    background: radial-gradient(ellipse at 50% 30%, var(--card-bg) 0%, var(--card-shade) 100%);
    box-shadow: 0 6px 18px rgba(0,0,0,0.18);
    overflow: hidden;
  }
  .card--back { left: 90px; top: 70px; }
  .card--front { left: 550px; top: 490px; }

  .brand-mark {
    display: flex;
    align-items: center;
    gap: 10px;
    font-weight: 700;
    font-size: 30px;
    letter-spacing: 0.5px;
    color: var(--brand-red);
    text-transform: uppercase;
    line-height: 1;
  }
  .brand-mark__square {
    width: 22px;
    height: 22px;
    background: var(--brand-blue);
  }

  .card--back .brand-mark {
    position: absolute;
    left: 50%;
    top: 118px;
    transform: translateX(-50%);
    white-space: nowrap;
  }
  .offer-list {
    position: absolute;
    left: 0;
    right: 0;
    top: 188px;
    margin: 0;
    padding: 0;
    list-style: none;
    text-align: center;
    font-size: 13px;
    color: var(--ink);
    line-height: 1.45;
  }

  .staff {
    position: absolute;
    right: 34px;
    top: 36px;
    text-align: right;
  }
  .staff__name {
    font-size: 20px;
    font-weight: 500;
    color: var(--accent-red);
    margin: 0;
    line-height: 1.1;
  }
  .staff__title {
    font-size: 13px;
    color: var(--ink);
    margin: 0;
  }

  .card--front .brand-mark {
    position: absolute;
    left: 44px;
    top: 122px;
  }

  .contact {
    position: absolute;
    left: 44px;
    top: 196px;
    font-size: 15px;
    color: var(--ink);
    line-height: 1.3;
  }
  .contact p { margin: 0; }
  .contact__row {
    display: flex;
    align-items: center;
    gap: 8px;
  }
  .contact__icon { width: 16px; height: 16px; flex: none; }

  .swoosh {
    position: absolute;
    left: 0;
    top: 0;
    width: 560px;
    height: 320px;
  }
  .swoosh__url {
    font-family: "Jost", sans-serif;
    font-size: 14px;
    fill: var(--soft-white);
    letter-spacing: 0.5px;
  }
</style>
</head>
<body>
<main class="canvas">

  <section class="card card--back" aria-label="Business card back">
    <div class="brand-mark"><span class="brand-mark__square"></span>Brindle Cove</div>
    <ul class="offer-list">
      <li>- a discount offer like 10% military and first responders</li>
      <li>- senior discount %5</li>
    </ul>
  </section>

  <section class="card card--front" aria-label="Business card front">
    <svg class="swoosh" viewBox="0 0 560 320" aria-hidden="true">
      <path d="M0,320 C170,292 360,230 560,112 L560,320 Z" fill="var(--accent-red)"/>
      <path d="M0,320 C175,298 365,238 560,120 L560,320 Z" fill="#ffffff"/>
      <path d="M0,320 C180,302 370,244 560,126 L560,320 Z" fill="var(--brand-blue)"/>
      <text class="swoosh__url" x="305" y="262" transform="rotate(-18 305 262)">brindlecove.com</text>
    </svg>

    <div class="staff">
      <p class="staff__name">Daniel Hart</p>
      <p class="staff__title">Manager</p>
    </div>

    <div class="brand-mark"><span class="brand-mark__square"></span>Brindle Cove</div>

    <div class="contact">
      <p>318 Orchard Lane</p>
      <p>Walworth, NY 14568</p>
      <p class="contact__row">
        <svg class="contact__icon" viewBox="0 0 16 16" aria-hidden="true">
          <path d="M2 6 C2 3 14 3 14 6 L12 7.5 L10.5 5.5 H5.5 L4 7.5 Z" fill="var(--brand-blue)"/>
          <rect x="4" y="8" width="8" height="6" rx="1.5" fill="var(--brand-blue)"/>
          <circle cx="8" cy="11" r="1.6" fill="#fff"/>
        </svg>
        585-437-9168
      </p>
      <p class="contact__row">
        <svg class="contact__icon" viewBox="0 0 16 16" aria-hidden="true">
          <rect x="1" y="3" width="14" height="10" fill="var(--brand-blue)"/>
          <path d="M1 3 L8 9 L15 3" fill="none" stroke="#fff" stroke-width="1.3"/>
        </svg>
        info@brindlecove.com
      </p>
    </div>
  </section>

</main>
</body>
</html>
```